Microsoft Word Sales Proposal Template

We'd like to produce a standard sales proposal template for Microsoft Word that better represents our company than our current template. Right now we have a very basic, dated look and feel to our template. We would like a proposal that graphically reflects our current branding, cleanly communicates the information contained in the proposal, and keeps the reader visually engaged with the text.

Our proposal documents consistently include the following hierarchy of information. We’d like a template designed to be flexible to change in this hierarchy, with a focus on cohesive design elements (heading fonts and styling, etc.):

- Cover Page
- Table of Contents
- Executive Summary
- Project Approach
- Sample Work/Select Clients List
- About Marlow Creek
- References
- Project Milestones and Budget
- Appendices

The primary focus is on the visual design elements: headers and footers, fonts, heading design consistency, and other graph and visual elements reflected in the attached proposal samples.

The Marlow Creek logo should not be altered in any way. I have attached 2 acceptable logos for use in the document. Client logos should also not be altered in any way. Placeholders for client logos in the template are appreciated for speed and accuracy of placement. Please avoid using cheesy stock photos.

For more information about our company and to review our current aesthetic, please visit http://www.marlowcreek-example.com/.
Updates

Thanks to everyone who has saved the project. We're excited to see your work. Please reach out if you need any clarifications or have questions.

Target Market(s)

Employees at large nonprofits who are responsible for technology decisions. Also target employees who create content and manage content for nonprofits.

Industry/Entity Type

It Company

Font styles to use
Serif
Sans Serif

Requirements
Must have
• Must Have:
• - Sample Table of Content
• - Representation of Section Headings
• - Clean design representative of our brand
• - Template elements that appropriately reflect each potential Table of Contents item
• - Easy flow of reading
• - Templates for reusable graphs and tables
• - Include 'Proprietary and Confidential' somewhere in footer to denote the confidentiality of proposal information
Should not have
• - cheesy stock images

```html
<!DOCTYPE html>
<html lang="en">
<head>
<meta charset="utf-8">
<title>NCA Project Approach – Marlow Creek</title>
<link rel="stylesheet" href="https://fonts.googleapis.com/css2?family=Open+Sans:ital,wght@0,600;1,400&family=Source+Sans+3:wght@300;400;600;700&display=swap">
<style>
  :root {
    --brand-blue: #0f5f98;
    --heading-blue: #1a6aa8;
    --quote-cyan: #6fd2f7;
    --body-grey: #585858;
    --rule-blue: #8fb4d4;
    --paper: #ffffff;
  }
  * { margin: 0; padding: 0; box-sizing: border-box; }
  html, body { width: 1200px; height: 800px; overflow: hidden; background: var(--paper); }
  body { font-family: "Source Sans 3", Arial, sans-serif; color: var(--body-grey); }
  .page { position: relative; width: 1200px; height: 800px; overflow: hidden; }

  .masthead { position: absolute; left: 0; top: 0; width: 508px; height: 213px; background: var(--brand-blue); padding: 42px 0 0 32px; }
  .masthead-title { font-family: "Open Sans", Arial, sans-serif; color: #fff; font-weight: 600; font-size: 28px; letter-spacing: 0.3px; line-height: 1; }
  .masthead-quote { font-family: "Open Sans", Arial, sans-serif; margin-top: 22px; width: 455px; color: var(--quote-cyan); font-style: italic; font-size: 16.5px; line-height: 24px; }
  .hero-photo { position: absolute; left: 511px; top: 0; width: 689px; height: 213px;
    background: linear-gradient(100deg, #e7eef0 0%, #cfd9dc 35%, #c9a98a 55%, #dfe5e6 75%, #c7d3d8 100%); }

  .intro { position: absolute; left: 97px; top: 250px; width: 466px; color: var(--heading-blue); font-size: 16px; line-height: 21px; text-align: justify; }

  .section-icon { position: absolute; left: 43px; top: 346px; width: 40px; height: 40px; }
  .section-heading { position: absolute; color: var(--heading-blue); font-weight: 300; font-size: 23px; line-height: 1; white-space: nowrap; border-bottom: 1px solid var(--heading-blue); padding-bottom: 5px; }
  .heading-develop { left: 84px; top: 349px; padding-left: 13px; padding-right: 2px; }
  .heading-train { left: 919px; top: 233px; width: 281px; }

  .copy { position: absolute; font-size: 12.2px; text-align: justify; }
  .copy strong { color: var(--heading-blue); font-weight: 700; }
  .copy-wide { left: 97px; top: 394px; width: 465px; line-height: 20.3px; }
  .copy-wide p + p { margin-top: 20px; }
  .copy-narrow { width: 246px; top: 282px; line-height: 17.6px; }
  .copy-narrow p + p { margin-top: 17.6px; }
  .copy-narrow p.run-on { margin-top: 0; }
  .col-enable { left: 634px; }
  .col-train { left: 921px; }
  .copy-narrow h3 { color: var(--heading-blue); font-size: 13px; font-weight: 700; line-height: 19px; }
  .copy a { color: var(--heading-blue); text-decoration: underline; }

  .footer-rule { position: absolute; top: 778px; height: 1px; background: var(--rule-blue); }
  .rule-left { left: 77px; width: 512px; }
  .rule-right { left: 606px; width: 510px; }
  .footer-mark { position: absolute; top: 756px; width: 36px; height: 36px; border-radius: 50%; background: var(--brand-blue); }
  .mark-left { left: 18px; }
  .mark-right { left: 1146px; }
  .footer-name { position: absolute; top: 762px; color: var(--brand-blue); font-size: 10px; font-weight: 600; }
  .name-left { left: 60px; }
  .name-right { right: 60px; }
  .footer-page { position: absolute; left: 540px; top: 761px; color: var(--heading-blue); font-size: 12.5px; }
  .footer-url { position: absolute; left: 629px; top: 761px; color: var(--heading-blue); font-size: 12.5px; }
</style>
</head>
<body>
<div class="page">
  <header class="masthead">
    <h1 class="masthead-title">NCA PROJECT APPROACH</h1>
    <p class="masthead-quote">“Although specific activities and deliverables will depend on the outcome of our discovery phase and the final creative designs, we propose the following approach to the NCA project. ”</p>
  </header>
  <div class="hero-photo" role="img" aria-label="Photograph of many raised hands giving a thumbs-up against a bright office background"></div>

  <p class="intro">We prefer to work in a highly collaborative fashion with our clients to ensure that we’re delivering what you need, when you need it, and within your organization’s budget.</p>

  <svg class="section-icon" viewBox="0 0 40 40" aria-hidden="true">
    <circle cx="20" cy="20" r="20" fill="#1b5f9b"/>
    <rect x="17" y="8" width="6" height="16" rx="3" fill="#fff"/>
    <circle cx="20" cy="30" r="3.2" fill="#fff"/>
  </svg>
  <h2 class="section-heading heading-develop">DEVELOP AND INTEGRATE</h2>

  <div class="copy copy-wide">
    <p><strong>Develop :</strong> And then, we build. While our end-to-end process involves discrete milestones and checkpoints, during the Develop stage, we tend to follow a more “agile” process, in order to give your team many opportunities for input and confirmation. Our philosophy is that once there’s something to show, we show it, in order to avoid surprises or misunderstandings that can be costly when discovered too far down the line. We ask our clients to play an active role as reviewers and collaborators during this phase, to make sure that we’re achieving the vision mapped together during the Design phase, and that we’re able to surface any new requirements or course-correct quickly together.</p>
    <p><strong>Integrate :</strong> As development progresses; we turn our attention to a parallel set of processes – getting all of your systems to connect. Whether it’s making an integrated view of your online and offline activities, connecting front-end content with back-end data, synching up advocacy or email solutions, exploring data warehousing, or smaller bits of integration like testing and tracking tools, we think about integration both in terms of data movement and also “use cases.” Our job is to uncover and project all the ways in which you might want to view, use, and manipulate your data, and to create easy integration and robust reporting that you can build on over time.</p>
  </div>

  <h2 class="section-heading heading-train">TRAIN AND ENABLE</h2>

  <div class="copy copy-narrow col-enable">
    <h3>Enable</h3>
    <p class="run-on">Our goal is to enable your organization to take complete, long-term ownership of these tools. Over the years, we have found that a “train the trainer” approach works best, in which we also do deep-dive training with one or more of your staff, giving them a masterful level of knowledge to facilitate in-house ownership of the system by your team. When a need for additional training arises, whether through staff turnover, change in roles, or a desire to go deeper with the tools, you can either utilize your in-house expert, or call on your Marlow Creek team.</p>
    <p>In addition to our custom approach, we often point clients to the vast repository of free resources out there that can help them extend their knowledge of open-source CMS tools such as Verdant CMS, of CRM concepts and the ins and outs of Cloudline CRM (including our own repository of videos on Quillbay.me: <a href="http://www.quillbay-example.me/">http://www.quillbay-example.me/)</a>, and of interesting best practices research, ideas, and resources that their team might find useful.</p>
  </div>

  <div class="copy copy-narrow col-train">
    <h3>Train</h3>
    <p class="run-on">To us, training is an ongoing activity that helps organizations take increasing ownership of the toolset and grow the ways they leverage Verdant CMS over time. We start training early in our projects by helping key staff to understand the conceptual model of Verdant CMS, so that they can play an active role with us in driving the technical solution.</p>
    <p class="run-on">However, a one-size-fits-all approach rarely matches the organizational complexities of modern nonprofits, where many individuals wear multiple hats; roles can be divided between departments; and interns, volunteers, or backups may need to cover critical tasks for the organization. As a project progresses, we shift our training activities to a more role-based approach that involves short, webcast training sessions by our project team. These sessions are customized for your specific tasks, such as the nuts-and-bolts of Cloudline CRM; content editing and maintenance; reconciling donations and sustainers; and the nitty gritty of how Launchpad and Cloudline CRM talk to each other.</p>
  </div>

  <footer>
    <span class="footer-mark mark-left" aria-hidden="true"></span>
    <span class="footer-name name-left">Marlow Creek</span>
    <span class="footer-rule rule-left"></span>
    <span class="footer-page">Page : 01</span>
    <span class="footer-url">www.marlowcreek-example.com</span>
    <span class="footer-rule rule-right"></span>
    <span class="footer-name name-right">Marlow Creek</span>
    <span class="footer-mark mark-right" aria-hidden="true"></span>
  </footer>
</div>
</body>
</html>
```